"Tidewell Kids" needs a A5 flyer for its "Art Contest"

Tidewell Kids needs a double sided A5 Flyer that illustrates in a child-friendly look the following competition:

Search for the up and coming Sprout Sketcher. The aim of our Sprout Sketcher is to allow our children to explore the artist within them and motivate them to express their talents through the fine art of drawing and painting.

Description: I have an art school, "Tidewell Kids", where children of 3-5 years old attend and learn how to paint and draw. We are making a competition where each child gets to draw a picture which we will upload to Friendloop and parents will vote for best picture. We need to distribute to the parents a flyer with following content.

Competition Name: Sprout Sketcher

Front Side (content):
No major text on the front. Only the Logo and messages grabbing the readers attention such as "Who will be our next Artist?", "Vote for your Child", "Like Us on our Friendloop Page".

Back Side (content):
Back side content is divided into 3 sections:

Section1:
How it Works?
Every child of every class will participate. Photos will be grouped by class.
There will be a Sprout Sketcher for each class, and there will be a Sprout Sketcher for the school.

Section2:
How to Participate?
In our search for ‘Sprout Sketcher’, we will select one piece of artwork from each child in the school, photograph it and upload it to our Friendloop page.
Vote for your favourite painting by following the steps below:
1- From your friendloop account go to www.friendloop-kids.net/Tidewell Kids
and “Like Us” to become a fan
2- Click on the“Sprout Sketcher” from the application menu
3- Browse through the different classes and vote for each picture you like
4- Invite your friends to vote for the picture you like to increase the chances of winning
The artist of the painting with most “Likes” will be crowned ‘Sprout Sketcher’.

Section3:
Note (in the footer):
Please note that the winner’s photo will be displayed in our “Sprout Sketcher” Frame on our Friendloop landing page. If you do not want your child’s photograph to be posted on our Friendloop page in this manner, please let us know by sending an e-mail.
, Tidewell Kids needs a double sided A5 Flyer that illustrates in a child-friendly look the following competition:

Front Side (content):

Back Side (content):

Section1:
How it Works?

Section2:
How to Participate?

Section3:
Note (in the footer):

Parents of the children attending at our school, Parents of the children attending at our school

Painting

• Colors used in the design should be strict to our logo colors. We have 4 colors in our logo feel free to use one or all of them through out the design:
#6CB53C
#DB2718
#5D9DD5
#F4D602

The elements in our logo are playful and hand drawn and written, so the flyer design should reflect the hand made style rather than solid elements and objects., Colors used in the design should be strict to our logo colors. We have 4 colors in our logo feel free to use one or all of them through out the design:
#6CB53C
#DB2718
#5D9DD5
#F4D602

The elements in our logo are playful and hand drawn and written, so the flyer design should reflect the hand made style rather than solid elements and objects.
• Images of real children., Images of real children.

```html
<!DOCTYPE html>
<html lang="en">
<head>
<meta charset="utf-8">
<title>Tidewell Kids – Sprout Sketcher Competition</title>
<link rel="stylesheet" href="https://fonts.googleapis.com/css2?family=Arvo:ital,wght@0,400;0,700;1,400&display=swap">
<style>
  :root {
    --teal: #287a8a;
    --orange: #f8a363;
    --orange-text: #f6a462;
    --green: #5aab2d;
    --red: #d9261c;
    --ink: #1f1f1f;
    --note: #9a9a9a;
    --white: #ffffff;
  }
  * { box-sizing: border-box; margin: 0; padding: 0; }
  html, body { width: 1200px; height: 850px; overflow: hidden; background: var(--white); }
  body { font-family: "Arvo", Georgia, serif; color: var(--ink); position: relative; }

  .front { position: absolute; left: 0; top: 0; width: 600px; height: 850px; overflow: hidden; }
  .front__painting {
    position: absolute; inset: 0;
    background:
      radial-gradient(ellipse 180px 220px at 260px 130px, rgba(232,110,50,.75), transparent 70%),
      radial-gradient(ellipse 260px 200px at 120px 620px, rgba(240,195,60,.55), transparent 70%),
      radial-gradient(ellipse 220px 200px at 470px 560px, rgba(70,110,170,.45), transparent 70%),
      radial-gradient(ellipse 200px 160px at 480px 260px, rgba(220,70,50,.35), transparent 70%),
      linear-gradient(160deg, #e9e6df 0%, #dcd8cf 50%, #e4dfd4 100%);
  }
  .front__brand {
    position: absolute; left: 0; top: 330px; width: 600px;
    text-align: center; color: var(--white);
    font-size: 68px; font-weight: 400; line-height: 1;
  }
  .front__band {
    position: absolute; left: 0; top: 658px; width: 600px; height: 99px;
    background: var(--teal); color: var(--white);
    display: flex; align-items: center; justify-content: center;
    font-size: 24px; letter-spacing: 1.2px;
  }
  .front__band span { color: var(--orange-text); }

  .back { position: absolute; left: 600px; top: 0; width: 600px; height: 850px; }
  .back__header {
    height: 135px; background: var(--teal); color: var(--white);
    display: flex; align-items: center; justify-content: center;
    font-size: 31px; letter-spacing: 1.5px; padding-top: 24px;
  }
  .back__header span { color: var(--orange-text); }

  .section-title { position: absolute; left: 41px; font-size: 20px; letter-spacing: 1px; font-weight: 400; }
  .section-title--works { top: 178px; color: var(--green); }
  .section-title--join { top: 275px; color: var(--red); }

  .copy { position: absolute; left: 41px; width: 520px; font-size: 12.4px; line-height: 16.5px; letter-spacing: .2px; }
  .copy--works { top: 218px; }
  .copy--join { top: 316px; }

  .steps { position: absolute; left: 67px; top: 375px; width: 500px; list-style: none; font-size: 12.4px; line-height: 16.5px; letter-spacing: .4px; }
  .steps li { padding-left: 20px; text-indent: -20px; margin-bottom: 16px; }

  .winner {
    position: absolute; left: 0; top: 563px; width: 600px; height: 140px;
    background: var(--orange); color: var(--teal);
    display: flex; align-items: center; justify-content: center; text-align: center;
    font-size: 19.5px; line-height: 25px; letter-spacing: .5px;
  }

  .note { position: absolute; left: 41px; top: 758px; width: 530px; color: var(--note); font-style: italic; font-size: 11.2px; line-height: 13.8px; }
</style>
</head>
<body>
  <section class="front">
    <div class="front__painting" role="img" aria-label="Colourful splattered paint artwork in orange, yellow, blue and green"></div>
    <div class="front__brand">Tidewell Kids</div>
    <div class="front__band">WHO WILL BE&nbsp;<span>OUR NEXT ARTIST?</span></div>
  </section>

  <section class="back">
    <header class="back__header">SPROUT SKETCHER&nbsp;<span>COMPETITION</span></header>

    <h2 class="section-title section-title--works">HOW IT WORKS?</h2>
    <p class="copy copy--works">Every child of every class will participate. Photos will be grouped by class.<br>There will be a Sprout Sketcher for each class, and there will be a<br>Sprout Sketcher for the school.</p>

    <h2 class="section-title section-title--join">HOW TO PARTICIPATE?</h2>
    <p class="copy copy--join">In our search for ‘Sprout Sketcher’, we will select one piece of artwork from each child in the school, photograph it and upload it to our Friendloop page. Vote for your favourite painting by following the steps below:</p>

    <ol class="steps">
      <li>1 - From your friendloop account go to www.friendloop-kids.net/Tidewell Kids and “Like Us” to become a fan</li>
      <li>2 - Click on the“Sprout Sketcher” from the application menu</li>
      <li>3 - Browse through the different classes and vote for each picture you like</li>
      <li>4 - Invite your friends to vote for the picture you like to increase the chances of winning</li>
    </ol>

    <div class="winner"><p>The artist of the painting with most “Likes”<br>will be crowned ‘Sprout Sketcher’.</p></div>

    <p class="note">Please note that the winner’s photo will be displayed in our “Sprout Sketcher” Frame on our Friendloop landing page. If you do not want your child’s photograph to be posted on our Friendloop page in this manner, please let us know by sending an e-mail.</p>
  </section>
</body>
</html>
```